Varnoth Lawyers needs a logo, business cards and stationery

we are a law firm that is new, progressive, energetic whilst still maintaining traditional values of the law. Our logo is attached. The square in the logo can be positioned above the name if required. The blue in the logo should be closer to a pantone PMS 2995 colour. Need business cards and letterhead and envelopes and with compliments slip. There is a separate contest for the business cards.
The business card should be double sided and i am looking to have a QR code either on the front or the back with contact information.
If you think you can do more with the logo, let me know.

The firm name is Varnoth Lawyers

Industry/Entity Type

Business

Font styles to use
Sans Serif

Colors
33a6d7

Requirements
Must have
• The stationery needs to have the firm name
• The physical address and a postal address
• webpage
Should not have
• Avoid any legal type images such as scales and columns etc, they seem to be overdone

```html
<!DOCTYPE html>
<html lang="en">
<head>
<meta charset="utf-8">
<title>Varnoth Lawyers – Letterhead</title>
<link rel="stylesheet" href="https://fonts.googleapis.com/css2?family=Arimo:wght@400;700&display=swap">
<style>
  :root {
    --brand-navy: #1b6193;
    --brand-cyan: #00b4e6;
    --icon-blue: #2aa7dc;
    --rule-grey: #cfd3d6;
    --contact-grey: #9aa3a9;
    --ink: #222426;
    --paper: #ffffff;
  }
  * { box-sizing: border-box; margin: 0; padding: 0; }
  html, body { width: 849px; height: 1200px; overflow: hidden; background: var(--paper); }
  body { font-family: "Arimo", Helvetica, Arial, sans-serif; color: var(--ink); }

  .letterhead { position: relative; width: 849px; height: 1200px; }

  .brand {
    position: absolute; left: 32px; top: 40px;
    display: flex; align-items: center; gap: 10px;
  }
  .brand-mark { width: 38px; height: 38px; background: var(--brand-navy); }
  .brand-name {
    font-size: 27px; font-weight: 400; color: var(--brand-navy);
    letter-spacing: 0.5px; line-height: 1;
  }

  .divider { position: absolute; top: 25px; width: 1px; height: 81px; background: #8fc9e6; }
  .divider.first { left: 302px; }
  .divider.second { left: 468px; }

  .contact-item {
    position: absolute; display: flex; align-items: flex-start; gap: 10px;
    font-size: 11.5px; line-height: 14px; color: var(--contact-grey);
  }
  .contact-item svg { flex: none; width: 17px; height: 17px; fill: none; stroke: var(--icon-blue); stroke-width: 1.3; }
  .contact-phone { left: 318px; top: 39px; }
  .contact-address { left: 318px; top: 69px; }
  .contact-email { left: 485px; top: 42px; }
  .contact-web { left: 485px; top: 71px; }

  .header-rule { position: absolute; left: 32px; top: 124px; width: 784px; height: 1px; background: var(--rule-grey); }

  .letter-body { position: absolute; left: 32px; top: 170px; width: 786px; }
  .letter-subject { font-size: 11.6px; font-weight: 700; line-height: 16px; margin-bottom: 22px; }
  .letter-body p { font-size: 11.1px; line-height: 25.9px; margin-bottom: 25.9px; }

  .footer-band { position: absolute; left: 0; bottom: 0; width: 849px; height: 13px; background: var(--brand-cyan); }
</style>
</head>
<body>
<main class="letterhead">
  <header>
    <div class="brand">
      <span class="brand-mark"></span>
      <span class="brand-name">Varnoth Lawyers</span>
    </div>

    <span class="divider first"></span>
    <span class="divider second"></span>

    <div class="contact-item contact-phone">
      <svg viewBox="0 0 20 20"><path d="M4 2.5l3 0.5 1.3 3.4-2 1.6c1 2.3 2.9 4.2 5.2 5.2l1.6-2 3.4 1.3 0.5 3c-0.2 1-1 1.6-2 1.5C8.6 16.4 3.6 11.4 2.5 4.5 2.4 3.5 3 2.7 4 2.5z"/></svg>
      <span>(626)-555-0148</span>
    </div>
    <div class="contact-item contact-address">
      <svg viewBox="0 0 20 20"><path d="M1.5 5l4.5-1.8 4 1.8 4-1.8 4.5 1.8v12l-4.5-1.8-4 1.8-4-1.8-4.5 1.8z"/><path d="M10 13.5s-3-3-3-5a3 3 0 0 1 6 0c0 2-3 5-3 5z"/><circle cx="10" cy="8.4" r="1"/></svg>
      <span>14 Harlow Street<br>Brindell, VIC 3290</span>
    </div>
    <div class="contact-item contact-email">
      <svg viewBox="0 0 20 20"><rect x="2" y="4.5" width="16" height="11"/><path d="M2 4.5l8 6.5 8-6.5M2 15.5l6-5M18 15.5l-6-5"/></svg>
      <span>j.carden@example.com</span>
    </div>
    <div class="contact-item contact-web">
      <svg viewBox="0 0 20 20"><circle cx="10" cy="10" r="8"/><ellipse cx="10" cy="10" rx="3.6" ry="8"/><path d="M2 10h16M3.2 6h13.6M3.2 14h13.6M10 2v16"/></svg>
      <span>www.example.com</span>
    </div>

    <div class="header-rule"></div>
  </header>

  <article class="letter-body">
    <h1 class="letter-subject">Lorem ipsum dolor sit amet, consectetur adipiscing elit.</h1>
    <p>Lorem ipsum dolor sit amet, consectetur adipiscing elit. Quisque bibendum ligula nulla, vel suscipit dolor accumsan ac. Maecenas in dolor nec turpis hendrerit efficitur in vitae ante. Nullam blandit nibh mattis sollicitudin rhoncus. Vestibulum sit amet ipsum erat. Morbi sodales et dolor ac convallis. Quisque a dolor purus. Nulla quis leo id mi dapibus sollicitudin.</p>
    <p>Donec bibendum gravida iaculis. Integer sit amet posuere tortor. Quisque eu nibh a mi tristique commodo. Sed dictum nunc sed magna ullamcorper, nec tincidunt dolor aliquam. Fusce ante arcu, rhoncus sed nisi id, convallis lacinia quam. Quisque porta efficitur iaculis. Nullam mauris nisl, gravida quis turpis quis, tincidunt dictum nunc. Sed auctor lacus eu nisi hendrerit scelerisque. Ut at lacinia lorem. Phasellus sed viverra eros, in semper nulla. Curabitur interdum dui ipsum, fermentum elementum orci iaculis id. In egestas tempus laoreet. Morbi fringilla, justo at dictum maximus, metus metus laoreet turpis, et vestibulum enim purus ac justo. Aenean vitae mauris sit amet urna accumsan blandit nec et magna. Quisque et nibh sagittis, dapibus magna ac, ullamcorper dui.</p>
    <p>Aliquam eget nulla nibh. Quisque porttitor placerat velit, vitae tempor urna volutpat sit amet. Cras sem libero, laoreet et mollis sit amet, mattis non leo. Vivamus ullamcorper mollis elit, nec ultrices nibh gravida id. Morbi hendrerit tortor quis nisl iaculis, vitae sodales massa mattis. Curabitur accumsan ante eu vulputate ultricies. Cras tellus nisl, lacinia vitae lectus eget, tempus vehicula tellus. Nunc egestas iaculis dolor, ac pellentesque justo imperdiet in. Nunc at est varius, sollicitudin velit quis, aliquet lacus. Proin vel elit non sem fermentum pulvinar vulputate sed lacus. Quisque elementum nisi a mattis auctor. Duis mollis, tortor in feugiat dignissim, purus nunc dapibus risus, ac fringilla purus erat nec felis. Vestibulum ante ipsum primis in faucibus orci luctus et ultrices posuere cubilia Curae;</p>
    <p>In fringilla lorem eu lectus viverra malesuada. Pellentesque ut vehicula augue. In sollicitudin enim elit, et rhoncus enim fringilla vel. Mauris eget scelerisque massa, a suscipit nisi. Nunc metus felis, porta eu nisl vitae, interdum dignissim arcu. Vestibulum quis est pellentesque, rhoncus enim iaculis, pellentesque nisl. Pellentesque habitant morbi tristique senectus et netus et malesuada fames ac turpis egestas. Duis auctor quis magna eu sodales. Duis et leo ac magna congue porttitor at eget justo. Nunc eu ante aliquam mi rutrum auctor vel in neque. Aliquam et felis vestibulum, pulvinar neque vitae, lacinia nulla. Morbi quis pulvinar velit, et ornare quam. Etiam vulputate turpis eros, vitae mollis elit cursus non. Etiam porttitor consequat varius.</p>
  </article>

  <footer class="footer-band"></footer>
</main>
</body>
</html>
```